Financial Services Company Needs New UI/UX

Hello!

We would like to see some UI/UX ideas for our software platform. I've attached a screen capture of our current "dashboard" (or main home page, essentially). We're looking for a very simple, clean, sleek design as there are many different pages throughout the system that will all need to coordinate. You can also view our website to see the colors and general "look" we have on there. It would be ideal for the portal to coordinate with the website since that is how they access the login page. Please submit your best ideas for the dashboard and we will reach out to our favorite designer to move forward with the rest of the pages. You can find our color hex codes on our website on the "Media" page. Should you need any other supporting logos or files please send us a message and we will try to accommodate.

Thanks!

Website: www.ledgerharbor-example.com

Target Market(s)

Our clients are contractors in the construction industry and our software helps them manage material purchases for their jobs.

Industry/Entity Type

Financial Service

Font styles to use
Sans Serif

Requirements
Must have
• The same content and language as the current dashboard but an updated look.
Should not have
• Too much distraction or busy patterns, we're looking for clean and simple and user friendly. Likely a solid or subtly textured background would be best.

```html
<!DOCTYPE html>
<html lang="en">
<head>
<meta charset="utf-8">
<title>LedgerHarbor Dashboard</title>
<link href="https://fonts.googleapis.com/css2?family=Open+Sans:wght@400;600;700&display=swap" rel="stylesheet">
<style>
:root{
  --page:#1f1f1f;
  --white:#ffffff;
  --ink:#2b2b2b;
  --dark:#333538;
  --orange:#e3601a;
  --orange-head:#e8651c;
  --red:#d24a48;
  --home:#d9443f;
  --gold:#e2a11b;
  --blue:#4f8fcf;
  --row-a:#e5e7f7;
  --row-b:#ebe3e5;
  --head-row:#f3f1f1;
  --grid:#d4d4dc;
  --link:#8a6b5a;
  --warn:#f2b705;
}
*{box-sizing:border-box;margin:0;padding:0}
html,body{width:1200px;height:1200px;overflow:hidden;background:var(--page);font-family:"Open Sans",sans-serif;color:var(--ink)}
.stage{position:absolute;left:0;top:292px;width:1414px;height:725px;transform:scale(0.84866);transform-origin:0 0;background:var(--white);overflow:hidden}
.topbar{position:absolute;left:0;top:0;width:1414px;height:67px;background:var(--white);border-bottom:1px solid #ddd}
.brand{position:absolute;left:12px;top:12px;display:flex;align-items:center;gap:10px;font-size:26px;color:var(--ink);letter-spacing:-0.3px}
.brand-dot{width:40px;height:40px;border-radius:50%;background:var(--blue)}
.contact{position:absolute;top:22px;display:flex;align-items:center;gap:8px;font-size:14px}
.contact svg{width:22px;height:22px}
.account{position:absolute;left:1112px;top:0;width:302px;height:67px;background:var(--orange-head);display:flex;align-items:center;color:var(--white);font-size:16px}
.account .caret{margin-left:30px;width:0;height:0;border-left:10px solid transparent;border-right:10px solid transparent;border-top:13px solid var(--white)}
.account .avatar{margin-left:26px;width:40px;height:40px;border-radius:50%;background:#8a6d5c;border:2px solid var(--white)}
.account .mail{margin-left:20px}
.menu{position:absolute;left:0;top:67px;width:1414px;height:29px;background:var(--dark);display:flex;align-items:center;color:var(--white);font-size:11px}
.menu-item{position:absolute;top:0;height:29px;display:flex;align-items:center;gap:10px}
.menu-item svg{width:16px;height:16px;fill:var(--white)}
.menu-item.is-active{background:var(--home);padding-left:18px}
.backdrop{position:absolute;left:0;top:96px;width:1414px;height:629px;background:linear-gradient(100deg,#c8cdec 0%,#e6e8f6 30%,#dfe2f2 62%,#f2c64a 82%,#e9a91a 100%)}
.panel{position:absolute;left:175px;top:108px;width:1059px;height:566px;background:var(--white)}
.dash-bar{position:absolute;left:17px;top:13px;width:1025px;height:34px;background:var(--red);color:var(--white);font-weight:600;font-size:13px;display:flex;align-items:center;padding-left:12px;gap:10px}
.dash-bar .toggle{position:absolute;right:0;top:0;width:36px;height:34px;background:var(--gold)}
.dash-bar .toggle::after{content:"";position:absolute;left:8px;top:12px;border-left:10px solid transparent;border-right:10px solid transparent;border-top:12px solid var(--white)}
.badge{display:inline-flex;align-items:center;justify-content:center;width:15px;height:15px;border-radius:50%;background:var(--warn);color:var(--white);font-size:10px;font-weight:700}
.badge.info{background:#e0421f}
.legend{position:absolute;left:19px;top:49px;font-size:10px;color:#444;display:flex;gap:10px;align-items:center}
.legend span{display:flex;align-items:center;gap:4px}
.tri{width:0;height:0;border-left:6px solid transparent;border-right:6px solid transparent;border-bottom:11px solid var(--warn)}
.card{position:absolute;top:85px;width:215px;height:164px;border-radius:3px;overflow:hidden;color:var(--white);text-align:center}
.card-head{height:33px;background:var(--dark);display:flex;align-items:center;gap:8px;padding-left:11px;font-weight:600;font-size:13px}
.card-body{height:131px;padding-top:9px}
.card.credit .card-body{background:var(--orange)}
.card.pay .card-body{background:var(--blue)}
.amount{font-size:22px;font-weight:700;line-height:28px}
.meta{font-size:10px;font-weight:700;line-height:12px;margin-top:9px}
.actions{display:flex;justify-content:center;gap:10px;position:absolute;bottom:18px;left:0;right:0}
.btn{background:var(--white);color:var(--ink);font-size:10px;font-weight:700;border-radius:12px;padding:5px 7px}
.grid{position:absolute;top:273px;width:504px;height:274px;border:1px solid var(--grid);overflow:hidden}
.grid-head{height:34px;background:var(--dark);color:var(--white);font-weight:600;font-size:12px;display:flex;align-items:center;gap:10px;padding-left:12px}
.grid table{width:100%;border-collapse:collapse;table-layout:fixed;font-size:9px;text-align:center}
.grid th{height:34px;background:var(--head-row);color:var(--link);font-weight:600;font-size:10px;text-decoration:underline;border-right:1px solid var(--grid)}
.grid td{height:30px;border-right:1px solid var(--grid);line-height:11px}
.grid tr:nth-child(odd) td{background:var(--row-a)}
.grid tr:nth-child(even) td{background:var(--row-b)}
</style>
</head>
<body>
<div class="stage">
  <header class="topbar">
    <div class="brand"><span class="brand-dot"></span>LedgerHarbor</div>
    <div class="contact" style="left:328px">
      <svg viewBox="0 0 24 24"><circle cx="12" cy="12" r="10" fill="none" stroke="#d9443f" stroke-width="2"/><path d="M8 7l2 0 1 3-1.5 1a6 6 0 0 0 3.5 3.5l1-1.5 3 1v2c-5 1-10-4-9-9z" fill="#d9443f"/></svg>
      Support :&nbsp;&nbsp;&nbsp;<span style="margin-left:10px">555-010-4477</span>
    </div>
    <div class="contact" style="left:546px">
      <svg viewBox="0 0 24 24"><circle cx="12" cy="12" r="10" fill="none" stroke="#f0a43a" stroke-width="2"/><rect x="6.5" y="8" width="11" height="8" fill="none" stroke="#f0a43a" stroke-width="1.6"/><path d="M6.5 8l5.5 4.5L17.5 8" fill="none" stroke="#f0a43a" stroke-width="1.6"/></svg>
      CustomerSupport@StonebridgeTrade.example
    </div>
    <div class="account"><span class="caret"></span><span class="avatar"></span><span class="mail">pc101@example.com</span></div>
  </header>

  <nav class="menu">
    <div class="menu-item is-active" style="left:0;width:109px"><svg viewBox="0 0 16 16"><path d="M8 1l7 7h-2v7h-4v-5H7v5H3V8H1z"/></svg>Home</div>
    <div class="menu-item" style="left:124px"><svg viewBox="0 0 16 16"><path d="M2 12l6-6 2 2-6 6zM9 2l5 5-2 2-5-5z"/></svg>Job Center</div>
    <div class="menu-item" style="left:246px"><svg viewBox="0 0 16 16"><rect x="1" y="4" width="14" height="8" rx="1" fill="none" stroke="#fff" stroke-width="1.5"/><circle cx="8" cy="8" r="2"/></svg>Payments</div>
    <div class="menu-item" style="left:372px"><svg viewBox="0 0 16 16"><path d="M8 1l7 4H1zM2 6h2v6H2zm4 0h2v6H6zm4 0h2v6h-2zM1 13h14v2H1z"/></svg>Credit Management</div>
    <div class="menu-item" style="left:530px"><svg viewBox="0 0 16 16"><path d="M3 1h7l3 3v11H3z" fill="none" stroke="#fff" stroke-width="1.5"/><path d="M5 7h6v1H5zm0 3h6v1H5z"/></svg>Prelien Center</div>
  </nav>

  <div class="backdrop" role="img" aria-label="Photo of architectural blueprints with a yellow hard hat and a hammer"></div>

  <main class="panel">
    <div class="dash-bar"><span class="badge">?</span>DASHBOARD<span class="toggle"></span></div>
    <div class="legend">
      <span><i class="tri"></i>Indicates an Action is Required</span>
      <span><i class="badge">?</i>Information only - no action required</span>
    </div>

    <section class="card credit" style="left:182px">
      <div class="card-head"><span class="badge info">i</span>Available Master Credit</div>
      <div class="card-body">
        <div class="amount">$1,29,500.00</div>
        <div class="meta">Master Credit Limit : 250,000.00</div>
        <div class="actions"><span class="btn">Setup New Job</span></div>
      </div>
    </section>
    <section class="card pay" style="left:407px">
      <div class="card-head"><span class="badge info">i</span>Last Payment</div>
      <div class="card-body">
        <div class="amount">$500.00</div>
        <div class="meta">Last Payment Date : 6/28/2016</div>
        <div class="actions"><span class="btn">View Payments</span><span class="btn">View Billings</span></div>
      </div>
    </section>
    <section class="card pay" style="left:633px">
      <div class="card-head"><i class="tri" style="margin-left:2px;margin-right:4px"></i>Next Payment</div>
      <div class="card-body">
        <div class="amount">$158.95</div>
        <div class="meta" style="margin-top:5px">Due Date : 6/28/2016<br>Current Principle : $9,968.46<br>Minimum Interest/Fees :&nbsp; $158.95</div>
        <div class="actions"><span class="btn">Make Payment</span></div>
      </div>
    </section>

    <section class="grid" style="left:16px">
      <div class="grid-head"><svg width="16" height="16" viewBox="0 0 16 16"><rect x="3" y="1" width="10" height="14" fill="none" stroke="#d9443f" stroke-width="1.5"/><path d="M5 5h6M5 8h6M5 11h6" stroke="#d9443f"/></svg>Task Summary</div>
      <table>
        <colgroup><col style="width:30px"><col style="width:190px"><col style="width:170px"><col></colgroup>
        <thead><tr><th></th><th>Task</th><th>Status</th><th>Received</th></tr></thead>
        <tbody>
          <tr><td><span class="badge">?</span></td><td>Supplier Invoice</td><td>Confirmation by Account Manager<br>Pending</td><td>5/1/2016</td></tr>
          <tr><td></td><td></td><td></td><td></td></tr>
          <tr><td></td><td></td><td></td><td></td></tr>
          <tr><td></td><td></td><td></td><td></td></tr>
          <tr><td></td><td></td><td></td><td></td></tr>
          <tr><td></td><td></td><td></td><td></td></tr>
          <tr><td></td><td></td><td></td><td></td></tr>
        </tbody>
      </table>
    </section>

    <section class="grid" style="left:538px">
      <div class="grid-head"><svg width="16" height="16" viewBox="0 0 16 16"><path d="M2 12l6-6 2 2-6 6zM9 2l5 5-2 2-5-5z" fill="#e2a11b"/></svg>Active Jobs</div>
      <table>
        <colgroup><col style="width:92px"><col style="width:115px"><col style="width:95px"><col style="width:103px"><col></colgroup>
        <thead><tr><th>Job#</th><th>Job Name</th><th>Status</th><th>Credit Limit</th><th>Avail. Credit</th></tr></thead>
        <tbody>
          <tr><td>pc101-001</td><td>Job#001</td><td>Active</td><td>$50,100.00</td><td>$35,100.00</td></tr>
          <tr><td>pc101-002</td><td>Job#002</td><td>Active</td><td>$40,000.00</td><td>$2,00.00</td></tr>
          <tr><td>pc101-003</td><td>Job#003</td><td>Active</td><td>$22,000.00</td><td>$0.00</td></tr>
          <tr><td>pc101-004</td><td>Job#004</td><td>Active</td><td>$10,400.00</td><td>$10,400.00</td></tr>
          <tr><td></td><td></td><td></td><td></td><td></td></tr>
          <tr><td></td><td></td><td></td><td></td><td></td></tr>
          <tr><td></td><td></td><td></td><td></td><td></td></tr>
        </tbody>
      </table>
    </section>
  </main>
</div>
</body>
</html>
```